Velm Biologics product brochure - credibility, sophistication, cutting-edge

Velm Biologics, Inc. is a company that provides the most cutting-edge regenerative medicine products in the US. This brochure will highlight our stem cell products VelmBase and VelmArc, educating the public/patients and physician alike on what stem cells are, comparison of various stem cell treatments available, and what makes Velm products different. This serves as a marketing tool to reach both patients and physicians.

I have included the current brochure, which I am not completely happy with. I want a brochure that portrays that we are a top-notch company, with credibility and sophistication. I will make slight content change, but most contents will stay.

Please refer to current website for further information: www.velmbiologics-example.com

Low design quality

Target Market(s)

doctors and patients.

Industry/Entity Type

Healthcare

Font styles to use
Serif
Other font styles liked:
• anything that looks best on brochures & easy to read

Colors

Designer to choose colors to be used in the design.

Requirements
Must have
• Clean & modern feel, eye-catching.
• Would prefer bi-fold rather than tri-fold, because I think it looks fresher.
• Easy to read, clear.
• beautiful, elegant, stunning
Should not have
• Please DO NOT recycle graphics or images from the old brochure. I would like this for sure to be brand new, fresh and original.

```html
<!DOCTYPE html>
<html lang="en">
<head>
<meta charset="utf-8">
<title>Velm Biologics Brochure Spread</title>
<link rel="stylesheet" href="https://fonts.googleapis.com/css2?family=Montserrat:wght@400;500;600;700&display=swap">
<style>
:root{
  --bg:#e9e7e3;
  --paper:#ffffff;
  --gold:#e8b94c;
  --gold-soft:#f2cf72;
  --gold-deep:#c9952e;
  --accent:#e0922a;
  --ink:#4a4a4a;
  --muted:#8a8a8a;
  --row:#fbf1da;
  --photo-grey:#9a9a9a;
}
*{box-sizing:border-box;margin:0;padding:0}
html,body{width:1200px;height:960px;overflow:hidden;background:var(--bg);font-family:"Montserrat",sans-serif;color:var(--ink)}
.spread{position:absolute;left:40px;top:200px;width:1120px;height:560px;display:flex;box-shadow:0 10px 30px rgba(0,0,0,.18)}
.page{position:relative;width:560px;height:560px;background:var(--paper);overflow:hidden}
.page--left{border-right:1px solid #e2e2e2}

/* left page */
.intro-panel{position:absolute;left:0;top:0;width:190px;height:400px;background:linear-gradient(160deg,var(--gold-deep),var(--gold) 55%,var(--gold-soft));padding:56px 22px 0 26px;color:#fff;font-size:12.5px;line-height:1.45;font-weight:500}
.runner-photo{position:absolute;left:0;top:400px;width:260px;height:160px;background:linear-gradient(180deg,#d6d6d6,#8f8f8f 70%,#6f6f6f)}
.products{position:absolute;left:214px;top:30px;width:320px;height:360px;font-size:8.6px;line-height:1.42}
.products h2{color:var(--accent);font-size:12px;font-weight:700;margin-bottom:6px}
.products ul{list-style:none;margin-bottom:8px}
.products li::before{content:"• "}
.products p{margin-bottom:8px}
.products .closing{color:var(--accent);font-weight:600;margin-bottom:0}
.sourcing{position:absolute;left:260px;top:400px;width:300px;height:160px;background:linear-gradient(135deg,var(--gold),var(--gold-soft))}
.sourcing svg{position:absolute;left:0;top:0}
.sourcing p{position:absolute;left:70px;top:26px;width:170px;text-align:center;color:#fff;font-size:8.5px;line-height:1.5}

/* right page */
.lead{position:absolute;left:200px;top:26px;width:330px;font-size:9px;line-height:1.5}
.lead h2{color:var(--accent);font-size:12px;font-weight:700;margin-bottom:5px}
.portrait{position:absolute;left:40px;top:40px;width:90px;height:90px}
.sources{position:absolute;left:24px;top:150px;width:512px}
.sources h3{color:var(--accent);font-size:12px;font-weight:700;text-align:center;margin-bottom:6px}
.sources table{width:100%;border-collapse:collapse;font-size:7.5px;line-height:1.35}
.sources th{color:var(--accent);font-weight:700;text-align:left;padding:3px 4px;font-size:8.5px}
.sources th small{display:block;font-size:6.5px;font-weight:500}
.sources td{padding:3px 4px;vertical-align:top;color:var(--ink)}
.sources td.label{font-weight:700;width:90px}
.sources td.auto{background:var(--row)}
.hands-photo{position:absolute;left:0;top:360px;width:560px;height:200px;background:linear-gradient(120deg,#7a5a26,#b99050 45%,#e6c98a 80%,#f3e3bd)}
.note{position:absolute;left:24px;top:372px;width:500px;color:#fff;font-size:7px;line-height:1.45}
</style>
</head>
<body>
<main class="spread">
  <section class="page page--left">
    <div class="intro-panel">Velm's regenerative medicine products provide a rich source of stem cell types including MSCs and hematopoietic stem cells (HSCs). They are crucial for tissue regeneration, with powerful anti-inflammatory, immunomodulatory and revascularization effects to maximize patients' healing potentials.</div>
    <div class="runner-photo" role="img" aria-label="Greyscale photo of a runner's legs wearing yellow shoes on a road"></div>
    <div class="products">
      <h2>Velm regenerative medicine products are:</h2>
      <ul>
        <li>Comprehensive: derived from umbilical cord tissue, cord blood and amniotic membrane</li>
        <li>Highly rich in mesenchymal stem cells (MSCs), which are known for their anti-inflammatory, immunomodulatory, anti-microbial, anti-apoptotic, revascularization properties</li>
        <li>With maximal preservation of the extracellular matrix and cytokines/growth factors that are crucial for tissue repair &amp; regeneration</li>
      </ul>
      <p>Umbilical cord-derived stem cells have a well-established safety record, require no HLA matching, and have a history of robust clinical research demonstrating benefits.</p>
      <p>Umbilical cord-derived stem cells have significant advantages over autologous stem cells:</p>
      <ul>
        <li>Younger, robust, more potent</li>
        <li>Higher self-renewal capacity</li>
        <li>More efficient differentiation</li>
        <li>Higher growth factor production</li>
        <li>Stronger anti-inflammatory effects</li>
        <li>More neuroprotective effects</li>
      </ul>
      <p class="closing">This makes Velm regenerative medicine products (VelmBase &amp; VelmArc) a preferred choice to be at the forefront of regenerative medicine.</p>
    </div>
    <div class="sourcing">
      <svg width="300" height="160" viewBox="0 0 300 160" aria-hidden="true"><polygon points="90,8 230,8 280,90 200,156 60,156 20,80" fill="none" stroke="#fff" stroke-width="1"/></svg>
      <p>Velm Biologics' regenerative medicine products are sourced from a FDA registered &amp; inspected cGMP compliant laboratory, which strictly follows ATSA (Allied Tissue Standards Association) guidelines, meeting the highest of industry standards.</p>
    </div>
  </section>

  <section class="page page--right">
    <svg class="portrait" viewBox="0 0 90 90" role="img" aria-label="Greyscale photo of a smiling couple in a diamond frame"><polygon points="45,0 90,45 45,90 0,45" fill="var(--photo-grey)"/></svg>
    <div class="lead">
      <h2>We're the cutting edge of stem cell therapy.</h2>
      <p>Umbilical cord-derived stem cells offer the best of both worlds: remarkably powerful cells due to their young age, and a history of excellent safety record. Velm Biologics is unique from other regenerative medicine companies because its products have the most comprehensive formulation of stem cells, high concentration of MSCs and the rich cytokines/growth factors from cord blood, cord tissue and amniotic membrane.</p>
    </div>
    <div class="sources">
      <h3>Stem Cell Sources and Pros &amp; Cons</h3>
      <table>
        <tr><th></th><th>Umbilical Cord</th><th>Amniotic</th><th>Autologous<small>(Adipose, Bone Marrow)</small></th></tr>
        <tr><td class="label">Stem Cell Type</td><td>MSC &amp; HSC</td><td>MSC &amp; Epithelial derived SSCs</td><td class="auto">MSC vs. MSC &amp; HSC</td></tr>
        <tr><td class="label">Concentration</td><td>Consistently high per individual product batch</td><td>Few live stem cells</td><td class="auto">1 to 50 million/cc, dependent on patient age and health</td></tr>
        <tr><td class="label">Quality of Cells</td><td>Young, robust, potent healing factors</td><td>Young, larger proportion of cellular debris</td><td class="auto">Quality declines with patient age &amp; disease</td></tr>
        <tr><td class="label">Adverse Reaction</td><td>Minimal</td><td>Minimal</td><td class="auto">Pain, risk of infection and other risks of surgical procedure</td></tr>
        <tr><td class="label">Consistency of Results</td><td>Consistent, based on quality of cells</td><td>Consistent, based on concentration</td><td class="auto">Variable, operator-dependent</td></tr>
        <tr><td class="label">Ease of Use</td><td>Thaw and infuse / inject</td><td>Thaw and infuse / inject</td><td class="auto">Surgical procedure and processing</td></tr>
        <tr><td class="label">Time in Office</td><td>60 minutes</td><td>60 minutes</td><td class="auto">3-5 hours</td></tr>
      </table>
    </div>
    <div class="hands-photo" role="img" aria-label="Warm golden-toned photo of a baby's hand holding an adult's finger"></div>
    <p class="note">Note: Velm's regenerative medicine products are intended for homologous use only. Outcomes vary between patients, and physicians should assess each case individually before treatment. Results described here reflect published research and are not a guarantee of individual outcome.</p>
  </section>
</main>
</body>
</html>
```